Wellness Web Design Project

web design for business called Brightmoor Wellness. I have a private practice for which i need patients. I teach in house and online courses for professional and the public. It will be both an educational site as well as a marketing site and it will have a store and a member login area. I do sonic acupuncture called velarics. It is based on pythagoras' music of the spheres. I use vibrational and harmonic therapies to harmonize cells psyches and souls! it is the most scientifically rooted of the alternative therapies available and i focus on womens health, pediatric, emotional problems and spiritual awakening. I need it to be a balance of spiritual and symbolic depth as well as being graceful sophisticated grounded. I want it to look incredibly elegant, sophisticated, and established, not airy fairy! i like a minimal approach, fresh air, clean, confident, expensive, luxurious but also playful. im not trying to mold myself into the usual framework. i am trying to convey a sense of unleashing power and purpose and pleasure. i need it to be Gorgeous and relatable while being original
i have included the site map as an upload and here is a link to all the things that a home page should include. I have the logo and other versions that i will use to promote the different online programs i have. I may have a 'sound logo' start as the page comes up. the sounds are ethereal tones rather than music and super gentle and mysterious without being cloying or overly emotional. I work with the physical body, emotional trauma and altered states so many hats and have many different prongs to what i do so organization and clarity is important without getting cluttered. want to convert and capture into my email list for sure and have free downloadable content to provide.
the logo i have designed speaks volumes about my aesthetic. i have included a flyer made - which is 1. direction, but i am interested in seeing some designs that play with white space as well. the 'look' of the flyer has never been published and so am in no way married to it. I will include some of the photo i will want to use along the way that give you some sense of things or things to riff off. some of the photos of me have alot of solid blocks of color... i have included one of them. I am very sensitive to sophistication of color.
the site map i have included is jsut my attempt to organize - i am not married to it!
thankyou so much, and if you haven;t yet discovered the power of sound to alter brain waves and cell functioning wherever you are in the world - I highly recommend it:)

Target Market(s)

women 25-55's educated, familiar with alternative healing and conscious living who have money to spend on wellness

Industry/Entity Type

Business

Requirements
Must have
• http://notes.plimtrove.example/guides/4821/9 Core-Parts-Of-A-Good-Landing-Page-Chart.aspx
these are some of the elements that seem to be necessary
plus social media links....

```html
<!DOCTYPE html>
<html lang="en">
<head>
<meta charset="utf-8">
<title>Brightmoor Wellness</title>
<link rel="stylesheet" href="https://fonts.googleapis.com/css2?family=Source+Sans+3:ital,wght@0,400;0,600;0,700;1,600&display=swap">
<style>
:root{
  --orange:#f28a00;
  --green:#2f8f3a;
  --green-text:#2a8a2f;
  --charcoal:#4a4a4a;
  --text:#4b4b4b;
  --line:#e3e3e3;
  --footer-band:#ebebeb;
  --white:#ffffff;
}
*{box-sizing:border-box;margin:0;padding:0}
html,body{width:1090px;height:1200px;overflow:hidden}
body{position:relative;background:var(--white);font-family:"Source Sans 3",sans-serif;color:var(--text)}
.abs{position:absolute}

.page-bg{left:0;top:150px;width:1090px;height:811px;background:linear-gradient(#efefef,#fbfbfb 30%,#fdfdfd)}

/* header */
.brand-mark{left:124px;top:30px;width:46px;height:46px;border-radius:50%;background:var(--orange)}
.brand-name{left:192px;top:36px;font-size:31px;font-weight:400;color:var(--orange);letter-spacing:1.5px;line-height:36px}
.login{left:896px;top:21px;width:71px;height:24px;border-radius:5px;background:linear-gradient(#5a5a5a,#2c2c2c);border:1px solid #888;color:#fff;font-size:10px;font-weight:700;display:flex;align-items:center;justify-content:center;gap:4px}
.search{left:754px;top:75px;width:219px;height:26px;border:1px solid #dcdcdc;border-radius:4px;background:#fafafa;font-size:11px;font-style:italic;color:#888;padding:6px 0 0 19px;letter-spacing:1px}
.search svg{position:absolute;right:6px;top:3px}

/* navigation */
.main-nav{left:118px;top:133px;width:854px;height:34px;border-radius:3px;background:linear-gradient(#42a94b,#2d8c36);display:flex;align-items:center;justify-content:space-between;padding:0 32px 0 27px;list-style:none}
.main-nav li{color:#fff;font-size:13px;font-weight:600;letter-spacing:.6px}
.main-nav li.current{color:#1d3d1f}

/* hero */
.hero{left:119px;top:179px;width:851px;height:316px;background:#fff;padding:4px;box-shadow:0 10px 14px -8px rgba(0,0,0,.35)}
.hero-panel{position:relative;width:100%;height:100%;background:linear-gradient(#fdb24c,#fdb04a 75%,#fd9d31)}
.hero-title{left:62px;top:22px;font-size:27px;font-weight:600;color:#444;letter-spacing:1.8px;line-height:32px}
.hero-lead{left:58px;top:72px;width:300px;font-size:14px;font-weight:600;line-height:18px;color:#fff;letter-spacing:.3px}
.benefits-title{left:58px;top:141px;font-size:18px;font-weight:600;color:#444;letter-spacing:.8px}
.benefits{left:58px;top:172px;list-style:none}
.benefits li{font-size:12.5px;font-weight:600;color:#fff;height:23px;display:flex;align-items:center;gap:7px;letter-spacing:.5px}
.btn{display:flex;align-items:center;justify-content:center;gap:8px;color:#fff;font-size:13px;font-weight:600;border-radius:2px;letter-spacing:.3px}
.btn-green{background:linear-gradient(#3fae4a,#2b8a34)}
.btn-dark{background:linear-gradient(#4a4a4a,#2f2f2f)}
.hero .btn-demo{left:56px;top:249px;width:136px;height:30px}
.hero .btn-trial{left:206px;top:249px;width:105px;height:30px}
.slider-prev{left:13px;top:155px}
.slider-next{left:821px;top:155px}
.video{left:387px;top:14px;width:403px;height:280px;background:#232323}
.video-frame{position:absolute;left:0;top:23px;width:403px;height:235px;background:linear-gradient(135deg,#2f3f55,#1e2b3d 55%,#3c4a5c)}
.play{position:absolute;left:175px;top:107px;width:68px;height:48px;border-radius:12px;background:linear-gradient(#d01a1a,#9c0e0e);display:flex;align-items:center;justify-content:center}

/* cards */
.card{width:273px;height:248px;top:532px;background:#fff;border:1px solid var(--line)}
.card h2{position:absolute;left:17px;top:14px;font-size:17.5px;font-weight:600;color:#3a3a3a;letter-spacing:.8px}
.card p{font-size:12px;line-height:15.5px;letter-spacing:.3px}
.photo{position:absolute;border:2px solid #fff;box-shadow:0 0 0 1px #ccc}
.author{left:114px;top:47px;font-size:13px;font-style:italic;font-weight:600;color:var(--orange)}
.meta{font-size:9.5px;font-style:italic;font-weight:600;color:var(--orange)}
.card .btn{position:absolute;height:30px}

/* badges */
.awards{left:118px;top:796px;width:854px;height:101px;background:#fff;border:1px solid var(--line);display:flex;align-items:center;justify-content:space-around;padding:0 20px}
.badge{width:120px;height:66px;border-radius:4px;background:#eeeeee}

.cta-demo{left:436px;top:915px;width:136px;height:30px}
.cta-trial{left:586px;top:915px;width:105px;height:30px}

/* footer */
.footer-band{left:0;top:961px;width:1090px;height:170px;background:var(--footer-band);border-top:2px solid #d6d6d6}
.newsletter{left:118px;top:975px;width:272px;height:141px;background:var(--orange)}
.newsletter h3{position:absolute;left:52px;top:12px;font-size:17px;font-weight:600;color:#fff;letter-spacing:.8px}
.newsletter .envelope{position:absolute;left:17px;top:18px}
.email-field{position:absolute;left:17px;top:45px;width:238px;height:28px;background:#fff;border:1px solid #ddd;border-radius:2px;font-size:10.5px;font-style:italic;color:#777;padding:7px 10px;letter-spacing:.6px}
.subscribe{position:absolute;left:162px;top:91px;width:93px;height:30px;background:linear-gradient(#555,#3a3a3a);border-radius:2px;color:#fff;font-size:12px;font-weight:600;display:flex;align-items:center;justify-content:center;letter-spacing:.6px}
.footer-heading{font-size:16.5px;font-weight:600;color:var(--orange);letter-spacing:.8px}
.socials{left:474px;top:1014px;display:flex;gap:6px}
.social{width:34px;height:34px;border-radius:5px}
.social.s1{background:#2a9fd8}.social.s2{background:#c9252b}.social.s3{background:#2c4f86}.social.s4{background:#1c6ea5}
.contact{left:713px;top:1006px;font-size:12.5px;line-height:18.2px;color:#444;letter-spacing:.3px;font-style:normal}
.contact .org{color:var(--green-text);font-weight:600}
.contact .val{color:var(--green-text)}
.bottom-bar{left:0;top:1131px;width:1090px;height:69px;background:var(--charcoal)}
.copyright{left:118px;top:1161px;font-size:10.5px;color:#e8e8e8;letter-spacing:.5px}
.footer-nav{right:118px;top:1161px;font-size:10.5px;color:#e8e8e8;letter-spacing:.5px;list-style:none;display:flex}
.footer-nav li+li::before{content:"|";margin:0 8px}
</style>
</head>
<body>
<div class="abs page-bg"></div>

<header>
  <div class="abs brand-mark"></div>
  <div class="abs brand-name">Brightmoor Wellness</div>
  <div class="abs login">
    <svg width="10" height="11" viewBox="0 0 10 11"><rect x="1" y="4.5" width="8" height="6" rx="1" fill="#f0b400"/><path d="M2.8 4.5V3a2.2 2.2 0 0 1 4.4 0v1.5" stroke="#ddd" stroke-width="1.3" fill="none"/></svg>
    Login »
  </div>
  <div class="abs search">Search..
    <svg width="28" height="20" viewBox="0 0 28 20"><circle cx="9" cy="8" r="6" stroke="#3fae4a" stroke-width="2.5" fill="none"/><path d="M13.5 12l8 6" stroke="#3fae4a" stroke-width="3.5" stroke-linecap="round"/></svg>
  </div>
</header>

<ul class="abs main-nav">
  <li class="current">Home</li><li>About Us</li><li>Our Treatments</li><li>Centers</li><li>Oriential Medicines</li><li>Contact Us</li>
</ul>

<section class="abs hero">
  <div class="hero-panel">
    <h1 class="abs hero-title">Brightmoor Wellness</h1>
    <p class="abs hero-lead">Lorem ipsum dolor amet, consectetuer adi sed diam nonummynibeu smod tincidunt magna aliquam.</p>
    <h3 class="abs benefits-title">Benifits</h3>
    <ul class="abs benefits">
      <li><svg width="13" height="11" viewBox="0 0 13 11"><path d="M1 6l4 3.5L12 1" stroke="#2f8f3a" stroke-width="2.6" fill="none"/></svg>Lorem ipsum dolor amet, consectetuer adi</li>
      <li><svg width="13" height="11" viewBox="0 0 13 11"><path d="M1 6l4 3.5L12 1" stroke="#2f8f3a" stroke-width="2.6" fill="none"/></svg>Lorem ipsum dolor amet, consectetuer adi</li>
      <li><svg width="13" height="11" viewBox="0 0 13 11"><path d="M1 6l4 3.5L12 1" stroke="#2f8f3a" stroke-width="2.6" fill="none"/></svg>Lorem ipsum dolor amet, consectetuer adi</li>
    </ul>
    <div class="abs btn btn-green btn-demo">Request a Demo <svg width="6" height="9" viewBox="0 0 6 9"><path d="M1 1l3.5 3.5L1 8" stroke="#fff" stroke-width="1.8" fill="none"/></svg></div>
    <div class="abs btn btn-dark btn-trial">Free Trial <svg width="6" height="9" viewBox="0 0 6 9"><path d="M1 1l3.5 3.5L1 8" stroke="#fff" stroke-width="1.8" fill="none"/></svg></div>
    <svg class="abs slider-prev" width="18" height="32" viewBox="0 0 18 32"><g fill="#fff"><circle cx="15" cy="2" r="1.6"/><circle cx="11" cy="7" r="1.6"/><circle cx="7" cy="12" r="1.6"/><circle cx="3" cy="16" r="1.6"/><circle cx="7" cy="20" r="1.6"/><circle cx="11" cy="25" r="1.6"/><circle cx="15" cy="30" r="1.6"/></g></svg>
    <svg class="abs slider-next" width="18" height="32" viewBox="0 0 18 32"><g fill="#333"><circle cx="3" cy="2" r="1.6"/><circle cx="7" cy="7" r="1.6"/><circle cx="11" cy="12" r="1.6"/><circle cx="15" cy="16" r="1.6"/><circle cx="11" cy="20" r="1.6"/><circle cx="7" cy="25" r="1.6"/><circle cx="3" cy="30" r="1.6"/></g></svg>
    <div class="abs video">
      <div class="video-frame" role="img" aria-label="Video still: hands holding a tuning fork over the knee">
        <div class="play"><svg width="24" height="24" viewBox="0 0 24 24"><path d="M4 2l18 10L4 22z" fill="#fff"/></svg></div>
      </div>
    </div>
  </div>
</section>

<section class="abs card" style="left:118px">
  <h2>Welcome to Our Website</h2>
  <div class="photo" role="img" aria-label="Portrait photo of the practitioner" style="left:18px;top:50px;width:83px;height:81px;background:linear-gradient(135deg,#8a5a3c,#c9a07e 60%,#efe6dc)"></div>
  <div class="abs author">Dr. Maren Hollis</div>
  <p class="abs" style="left:114px;top:69px;width:150px">Lorem ipsum dolor amet, adipiscing elit, diam. Lore m ipsum dolor amet, adip iscing elit, diam.</p>
  <p class="abs" style="left:21px;top:141px;width:240px;line-height:17.5px">Lorem ipsum dolor amet, a dipiscing elit, diam. Lorem ipsum dolor amet, adipiscing elit, diam.</p>
  <div class="btn btn-green" style="left:151px;top:201px;width:106px">Read More</div>
</section>

<section class="abs card" style="left:408px">
  <h2 style="left:20px">What Our Customer Says</h2>
  <div class="photo" role="img" aria-label="Customer portrait photo" style="left:19px;top:50px;width:73px;height:58px;background:linear-gradient(135deg,#6b5344,#c8a994 55%,#e7e2dc)"></div>
  <p class="abs" style="left:102px;top:54px;width:160px">Lorem ipsum dolor amet, av adipiscing elit, sed diam.</p>
  <div class="abs meta" style="left:106px;top:98px">about 5 hours ago from web</div>
  <div class="photo" role="img" aria-label="Customer portrait photo" style="left:19px;top:133px;width:73px;height:57px;background:linear-gradient(135deg,#5c6a3a,#d7b98d 55%,#efe4d2)"></div>
  <p class="abs" style="left:104px;top:136px;width:160px;line-height:20px">Lorem ipsum dolor amet, av adipiscing elit, sed diam.</p>
  <div class="abs meta" style="left:104px;top:179px">about 9 hours ago from web</div>
  <div class="btn btn-green" style="left:155px;top:201px;width:106px">Read All</div>
</section>

<section class="abs card" style="left:699px">
  <h2 style="top:10px">What We Offers</h2>
  <div class="photo" role="img" aria-label="Photo of a woman reading a book" style="left:16px;top:41px;width:238px;height:130px;background:linear-gradient(110deg,#e9e3d6,#d9b89a 40%,#3f6a72 70%,#a0633b)"></div>
  <div class="btn btn-green" style="left:54px;top:201px;width:166px">View More Resources</div>
</section>

<section class="abs awards" aria-label="Awards and recognitions">
  <div class="badge" role="img" aria-label="Award badge"></div>
  <div class="badge" role="img" aria-label="Award badge" style="width:80px"></div>
  <div class="badge" role="img" aria-label="Award badge"></div>
  <div class="badge" role="img" aria-label="Award badge"></div>
  <div class="badge" role="img" aria-label="Award badge" style="width:140px"></div>
</section>

<div class="abs btn btn-green cta-demo">Request a Demo <svg width="6" height="9" viewBox="0 0 6 9"><path d="M1 1l3.5 3.5L1 8" stroke="#fff" stroke-width="1.8" fill="none"/></svg></div>
<div class="abs btn btn-dark cta-trial">Free Trial <svg width="6" height="9" viewBox="0 0 6 9"><path d="M1 1l3.5 3.5L1 8" stroke="#fff" stroke-width="1.8" fill="none"/></svg></div>

<footer>
  <div class="abs footer-band"></div>
  <div class="abs newsletter">
    <svg class="envelope" width="23" height="15" viewBox="0 0 23 15"><rect x="1" y="1" width="21" height="13" fill="none" stroke="#fff" stroke-width="1.6"/><path d="M1 1l10.5 8L22 1" fill="none" stroke="#fff" stroke-width="1.6"/></svg>
    <h3>Newsletter Sign Up</h3>
    <div class="email-field">Enter Your Email..</div>
    <div class="subscribe">Subscribe</div>
  </div>
  <div class="abs footer-heading" style="left:479px;top:977px">Follow Us</div>
  <div class="abs socials">
    <div class="social s1" role="img" aria-label="Social link"></div>
    <div class="social s2" role="img" aria-label="Social link"></div>
    <div class="social s3" role="img" aria-label="Social link"></div>
    <div class="social s4" role="img" aria-label="Social link"></div>
  </div>
  <div class="abs footer-heading" style="left:712px;top:977px">Contact Us</div>
  <address class="abs contact">
    <div class="org">Brightmoor Wellness</div>
    <div>418 Larkspur Lane,</div>
    <div>Fairhaven,&nbsp; OR 97031, United States</div>
    <div>Phone : <span class="val">0800 555 0142</span></div>
    <div>Fax :&nbsp;&nbsp;&nbsp;&nbsp; <span class="val">0800 555 0142</span></div>
    <div>Email :&nbsp; <span class="val">info@brightmoorwellness</span></div>
  </address>
  <div class="abs bottom-bar"></div>
  <div class="abs copyright">Copyright©2013 Brightmoor wellness. All right Reserved</div>
  <ul class="abs footer-nav">
    <li>Home</li><li>About Us</li><li>Our Treatments</li><li>Centers</li><li>Oriential Medicines</li><li>Contact Us</li>
  </ul>
</footer>
</body>
</html>
```